Criação de Papelaria Profissional para Advocacia e Direito
A empresa queria:
" Escritório com atuação perante empresários. Trabalhamos com assessoria jurídica para empresas em mais de 3 estados. "

```html
<!DOCTYPE html>
<html lang="pt-BR">
<head>
<meta charset="utf-8">
<title>Castelo Nunes Advocacia — Pasta Institucional</title>
<link href="https://fonts.googleapis.com/css2?family=Montserrat:wght@400;500;600&display=swap" rel="stylesheet">
<style>
  :root {
    --backdrop: #1c1c1c;
    --paper: #f4f4f2;
    --ink: #1f1f1f;
    --on-dark: #e9e9e7;
    --on-dark-muted: #a9a9a6;
    --on-light-muted: #6b6b68;
    --fold: rgba(0,0,0,0.12);
  }
  * { margin: 0; padding: 0; box-sizing: border-box; }
  html, body {
    width: 1200px; height: 1200px; overflow: hidden;
    background: var(--backdrop);
    font-family: "Montserrat", sans-serif;
  }
  .canvas {
    width: 1200px; height: 1200px;
    display: flex; flex-direction: column; align-items: center; justify-content: center;
    gap: 70px;
  }
  .spread {
    display: flex; width: 680px; height: 480px;
    box-shadow: 0 20px 50px rgba(0,0,0,0.5);
  }
  .page { position: relative; width: 340px; height: 480px; overflow: hidden; }
  .page--dark { background: var(--ink); }
  .page--light { background: var(--paper); }
  .page--light + .page--light { border-left: 1px solid var(--fold); }

  .firm-name { display: flex; flex-direction: column; align-items: flex-start; white-space: nowrap; }
  .firm-name__title {
    font-weight: 500; font-size: 14px; line-height: 1.2; letter-spacing: 0.12em;
    text-transform: uppercase;
  }
  .firm-name__note {
    font-weight: 500; font-size: 6px; letter-spacing: 0.3em; text-transform: uppercase;
    margin-top: 4px;
  }

  .cover-front .firm-name {
    position: absolute; top: 172px; left: 50%; transform: translateX(-50%);
    align-items: center; color: var(--ink);
  }
  .cover-front .firm-name__note { color: var(--on-light-muted); }

  .cover-back .contact {
    position: absolute; left: 22px; bottom: 24px; right: 22px;
    display: flex; justify-content: space-between; align-items: flex-end;
    color: var(--on-dark-muted); font-size: 5px; line-height: 1.8; letter-spacing: 0.04em;
  }
  .contact__col { display: flex; flex-direction: column; }
  .contact__item { display: flex; align-items: center; gap: 4px; }
  .contact__icon { width: 6px; height: 6px; flex: none; }
  .contact__dot { width: 6px; height: 6px; border-radius: 50%; background: var(--on-dark-muted); flex: none; }
  .cover-back .firm-name { color: var(--on-dark); }
  .cover-back .firm-name__title { font-size: 6.5px; letter-spacing: 0.1em; }
  .cover-back .firm-name__note { font-size: 3.5px; margin-top: 2px; color: var(--on-dark-muted); }

  .pocket { position: absolute; left: 0; bottom: 0; width: 340px; height: 200px; }
  .pocket svg { display: block; }
  .pocket .firm-name {
    position: absolute; right: 30px; bottom: 74px; color: var(--on-dark);
  }
  .pocket .firm-name__title { font-size: 11px; }
  .pocket .firm-name__note { color: var(--on-dark-muted); font-size: 5px; }
</style>
</head>
<body>
<main class="canvas">

  <section class="spread spread--outer" aria-label="Capa e contracapa da pasta">
    <div class="page page--dark cover-back">
      <div class="contact">
        <div class="contact__col">
          <span class="contact__item">
            <svg class="contact__icon" viewBox="0 0 10 10"><path d="M2 1h2l1 2.5-1.3 1a6 6 0 0 0 2.8 2.8l1-1.3L10 7v2a1 1 0 0 1-1 1A8 8 0 0 1 1 2a1 1 0 0 1 1-1z" fill="#a9a9a6"/></svg>
            +55 11 4000-2188
          </span>
          <span class="contact__item">contato@castelonunes.adv.br</span>
          <span class="contact__item"><span class="contact__dot"></span>@castelonunes</span>
        </div>
        <div class="contact__col">
          <span>Rua das Acácias, 480 · Sala 12</span>
          <span>Centro · São Paulo · SP</span>
          <span>www.castelonunes.adv.br</span>
        </div>
        <div class="firm-name">
          <span class="firm-name__title">Castelo Nunes</span>
          <span class="firm-name__note">Advocacia Empresarial</span>
        </div>
      </div>
    </div>
    <div class="page page--light cover-front">
      <div class="firm-name">
        <span class="firm-name__title">Castelo Nunes</span>
        <span class="firm-name__note">Advocacia Empresarial</span>
      </div>
    </div>
  </section>

  <section class="spread spread--inner" aria-label="Parte interna da pasta com bolso">
    <div class="page page--light inner-left"></div>
    <div class="page page--light inner-right">
      <div class="pocket">
        <svg width="340" height="200" viewBox="0 0 340 200" aria-hidden="true">
          <path d="M0 200 L0 150 C0 60 60 20 150 20 L340 20 L340 200 Z" fill="#1f1f1f"/>
        </svg>
        <div class="firm-name">
          <span class="firm-name__title">Castelo Nunes</span>
          <span class="firm-name__note">Advocacia Empresarial</span>
        </div>
      </div>
    </div>
  </section>

</main>
</body>
</html>
```